Brand new redesign of Brightwell finance website

I need a new website design that i can advertise a great low interest rate on the front page and capture input application details that will send through to my email address.

some car finance companies will be similar to this would be listed below

tallyfunds.com.au
corelinefinance.com.au
finance715.com.au
wexburyfinance.com.au
finance93.com.au

Reason: I have changed the project to a committed project. all the webpages should have the same format just different content and i want to be able to edit the front page easily to update my interest rates.

Reason: Provide more time for resubmission and submission work

Target Market(s)

Australian Finance market targeting a younger demographic

Industry/Entity Type

Finance

Coding

Coded - Design and coding required

Number of Pages Required

5+ page

Font styles to use
Serif
Sans Serif

Colors
0255a3
ffffff
cedeed

Requirements
Must have
• application capture form
• apply now buttons
• Headline rate front page

```html
<!DOCTYPE html>
<html lang="en">
<head>
<meta charset="utf-8">
<title>Brightwell Finance</title>
<link href="https://fonts.googleapis.com/css2?family=Open+Sans:wght@300;400;600;700&display=swap" rel="stylesheet">
<style>
:root{
  --brand:#0255a3;
  --navy:#0d2b7a;
  --ink:#333a44;
  --muted:#5b6270;
  --white:#ffffff;
  --pale:#cedeed;
  --footer:#262b38;
  --footer-text:#9aa0ab;
  --rule:#d8dbe0;
}
*{box-sizing:border-box;margin:0;padding:0}
html,body{width:766px;height:1200px;overflow:hidden;background:var(--white)}
body{font-family:"Open Sans",Arial,sans-serif;color:var(--ink);position:relative}
.page{position:relative;width:766px;height:1200px;overflow:hidden}
.abs{position:absolute}

/* header */
.topline{left:0;top:0;width:766px;height:2px;background:var(--brand)}
.header{left:0;top:2px;width:766px;height:90px;background:var(--white);box-shadow:0 1px 3px rgba(0,0,0,.25);z-index:2}
.brand{left:63px;top:24px;display:flex;align-items:center;gap:8px}
.brand-mark{width:30px;height:30px;border-radius:50%;background:var(--navy)}
.brand-name{font-size:15px;font-weight:700;color:var(--navy);letter-spacing:.3px}
.search{left:577px;top:17px;width:125px;height:24px;border:1px solid var(--rule);font-size:7px;color:#9aa0ab;padding:7px 6px}
.search svg{position:absolute;right:6px;top:7px}
.nav{top:59px;left:0;width:766px;font-size:8.5px;color:#222}
.nav span{position:absolute;white-space:nowrap}
.nav .active{color:var(--navy)}

/* hero */
.hero{left:0;top:92px;width:766px;height:311px;background:linear-gradient(120deg,#c9a79c 0%,#e2d6d0 35%,#cfd3d9 60%,#9fb2cc 85%,#c8d0dc 100%)}
.hero-title{left:63px;top:187px;font-size:28px;font-weight:700;color:var(--white);letter-spacing:.5px;text-shadow:0 1px 3px rgba(0,0,0,.3)}
.hero-sub{left:63px;top:222px;font-size:22px;font-weight:600;color:var(--white);text-shadow:0 1px 3px rgba(0,0,0,.3)}
.btn-apply{left:63px;top:267px;width:100px;height:29px;background:var(--navy);color:var(--white);font-size:10.5px;font-weight:600;display:flex;align-items:center;justify-content:center;gap:9px;border:1px solid #3a5fb0}

/* welcome */
.centered{left:0;width:766px;text-align:center}
.welcome-title{top:421px;font-size:15px;font-weight:600;color:#444}
.welcome-title b{color:var(--navy);font-weight:600}
.welcome-text{top:448px;left:74px;width:618px;font-size:7.6px;line-height:16px;color:var(--muted);text-align:center}

/* features */
.features{left:0;top:522px;width:766px;height:230px;background:linear-gradient(90deg,#1f5596 0%,#2d6aae 40%,#3f7cc0 70%,#2a66ab 100%)}
.feat-title{top:542px;font-size:14px;font-weight:600;color:var(--white)}
.feat-sub{top:572px;font-size:7.6px;color:var(--white)}
.feature{top:602px;width:150px;text-align:center;color:var(--white)}
.feature svg{display:block;margin:0 auto}
.feature h3{font-size:11px;font-weight:400;margin-top:11px}
.feature p{font-size:7.6px;line-height:13.6px;margin-top:6px;color:#e4ecf6}

/* testimonial */
.quote-title{top:771px;font-size:11.5px;font-weight:600;color:var(--brand)}
.quote-text{top:796px;left:88px;width:590px;font-size:7.6px;line-height:16px;color:var(--muted);text-align:center}
.avatar{left:352px;top:840px;width:62px;height:62px;border-radius:50%;border:2px solid #cfd3d9;background:linear-gradient(180deg,#dfe3e8,#8b95a3)}
.person-name{top:910px;font-size:8.5px;font-weight:700;color:var(--brand)}
.person-role{top:925px;font-size:7px;color:#333}
.dots{left:364px;top:945px;display:flex;gap:2px}
.dots i{display:block;width:12px;height:2px;background:#444}
.dots i:first-child{background:var(--brand)}

/* footer */
.footer{left:0;top:965px;width:766px;height:235px;background:var(--footer)}
.f-title{top:995px;font-size:13px;font-weight:400;color:var(--white)}
.field{height:20px;width:129px;background:var(--white);border-radius:2px;font-size:6.5px;color:#8a8f98;padding:6px 10px}
.check{left:207px;top:1095px;font-size:6.5px;color:var(--footer-text);display:flex;align-items:center;gap:5px}
.check i{display:block;width:7px;height:7px;border:1px solid #555d6b;border-radius:1px}
.btn-signup{left:204px;top:1122px;width:129px;height:22px;background:var(--brand);color:var(--white);font-size:9.5px;font-weight:700;display:flex;align-items:center;justify-content:center;border-radius:2px}
.f-text{left:376px;top:1022px;width:250px;font-size:6.5px;line-height:13px;color:var(--footer-text)}
.contact-line{left:376px;top:1073px;font-size:10px;color:var(--white)}
.contact-line span{color:#3f8ad8;font-size:8px}
.social{left:377px;top:1101px;font-size:9px;color:var(--white);display:flex;align-items:center;gap:8px}
.social i{display:block;width:18px;height:18px;border-radius:50%;background:#6b7280}
.f-links{left:651px;top:1022px;font-size:7px;line-height:16px;color:var(--footer-text);list-style:none}
.copyright{top:1175px;font-size:7px;color:var(--footer-text)}
</style>
</head>
<body>
<div class="page">
  <div class="abs topline"></div>
  <header class="abs header">
    <div class="abs brand"><span class="brand-mark"></span><span class="brand-name">BRIGHTWELL FINANCE</span></div>
    <div class="abs search">Search
      <svg width="9" height="9" viewBox="0 0 10 10"><circle cx="4" cy="4" r="3" fill="none" stroke="#9aa0ab" stroke-width="1.2"/><line x1="6.2" y1="6.2" x2="9" y2="9" stroke="#9aa0ab" stroke-width="1.2"/></svg>
    </div>
    <nav class="abs nav">
      <span class="active" style="left:364px">HOME</span>
      <span style="left:421px">ABOUT US</span>
      <span style="left:495px">HOW IT WORKS</span>
      <span style="left:586px">SERVICES</span>
      <span style="left:654px">CONTACT US</span>
    </nav>
  </header>

  <section class="abs hero" role="img" aria-label="Close-up photo of hands reviewing financial charts with a pen"></section>
  <h1 class="abs hero-title">LOW RATES FROM 5.49%</h1>
  <p class="abs hero-sub">comparison rate 5.89% p.a. on car loans</p>
  <a class="abs btn-apply">APPLY NOW
    <svg width="11" height="11" viewBox="0 0 12 12"><circle cx="6" cy="6" r="6" fill="#fff"/><path d="M5 3.5 L7.5 6 L5 8.5" fill="none" stroke="#0d2b7a" stroke-width="1.6"/></svg>
  </a>

  <h2 class="abs centered welcome-title">WELCOME TO <b>BRIGHTWELL FINANCE</b></h2>
  <p class="abs welcome-text">Sed ut perspiciatis unde omnis iste natus error sit voluptatem accusantium doloremque laudantium, totam rem aperiam, eaque ipsa quae ab illo inventore veritatis et quasi architecto beatae vitae dicta sunt explicabo. Nemo enim ipsam voluptatem quia voluptas sit aspernatur aut odit aut fugit, sed quia consequuntur magni dolores neque porro quisquam est, qui dolorem eos qui ratione voluptatem sequi nesciunt.</p>

  <section class="abs features" role="img" aria-label="Blurred blue photo of an office desk with documents"></section>
  <h2 class="abs centered feat-title">FEATURE SERVICES</h2>
  <p class="abs centered feat-sub">Sed ut perspiciatis unde omnis iste natus error sit voluptatem accusantium doloremque</p>

  <div class="abs feature" style="left:65px">
    <svg width="62" height="58" viewBox="0 0 62 58"><ellipse cx="31" cy="29" rx="28" ry="25" fill="none" stroke="#fff" stroke-width="2.5" transform="rotate(-30 31 29)"/><path d="M19 28 Q31 14 43 28 Z" fill="#fff"/><path d="M31 28 V38 Q31 41 28 40" fill="none" stroke="#fff" stroke-width="2"/></svg>
    <h3>Bas Agent</h3>
    <p>Sed ut perspiciatis unde omnis iste natus error sit voluptatem accusantium doloremque laudantium totam.</p>
  </div>
  <div class="abs feature" style="left:228px">
    <svg width="62" height="58" viewBox="0 0 62 58"><ellipse cx="31" cy="29" rx="28" ry="25" fill="none" stroke="#1b2f7a" stroke-width="2.5" transform="rotate(-30 31 29)"/><rect x="21" y="21" width="17" height="17" rx="2" fill="none" stroke="#1b2f7a" stroke-width="2.2"/><path d="M24 28 L29 33 L40 20" fill="none" stroke="#1b2f7a" stroke-width="2.6"/></svg>
    <h3>Payroll</h3>
    <p>Sed ut perspiciatis unde omnis iste natus error sit voluptatem accusantium doloremque laudantium totam.</p>
  </div>
  <div class="abs feature" style="left:392px">
    <svg width="62" height="58" viewBox="0 0 62 58"><ellipse cx="31" cy="29" rx="28" ry="25" fill="none" stroke="#1b2f7a" stroke-width="2.5" transform="rotate(-30 31 29)"/><rect x="20" y="23" width="22" height="15" rx="2" fill="#1b2f7a"/><rect x="27" y="19" width="8" height="5" fill="none" stroke="#1b2f7a" stroke-width="1.8"/><line x1="20" y1="30" x2="42" y2="30" stroke="#3f7cc0" stroke-width="1"/></svg>
    <h3>Credit File Repair</h3>
    <p>Sed ut perspiciatis unde omnis iste natus error sit voluptatem accusantium doloremque laudantium totam.</p>
  </div>
  <div class="abs feature" style="left:557px">
    <svg width="62" height="58" viewBox="0 0 62 58"><ellipse cx="31" cy="29" rx="28" ry="25" fill="none" stroke="#1b2f7a" stroke-width="2.5" transform="rotate(-30 31 29)"/><rect x="23" y="18" width="10" height="14" fill="#1b2f7a"/><path d="M28 24 H36 L40 28 V40 H28 Z" fill="none" stroke="#1b2f7a" stroke-width="2"/></svg>
    <h3>Dep Consolidation</h3>
    <p>Sed ut perspiciatis unde omnis iste natus error sit voluptatem accusantium doloremque laudantium totam.</p>
  </div>

  <h2 class="abs centered quote-title">AT VERO EOS ET ACCUSAMUS</h2>
  <p class="abs quote-text">Lorem ipsum dolor sit amet, consectetuer adipiscing elit, sed diam nonummy nibh euismod tincidunt ut laoreet dolore magna aliquam erat volutpat. Nam vitae euismod ipsum nec, placerat turpis. Aenean eu gravida arcu, et consectetur orci Quisque posuere dolor in malesuada fermentum.</p>
  <div class="abs avatar" role="img" aria-label="Portrait photo of a client in a suit"></div>
  <p class="abs centered person-name">OWEN MARSH</p>
  <p class="abs centered person-role">Business Man</p>
  <div class="abs dots"><i></i><i></i><i></i></div>

  <footer class="abs footer"></footer>
  <h3 class="abs f-title" style="left:63px">A Quick Contact Form</h3>
  <div class="abs field" style="left:63px;top:1030px">Business Name</div>
  <div class="abs field" style="left:204px;top:1030px">Contact Name</div>
  <div class="abs field" style="left:63px;top:1059px">Email Address</div>
  <div class="abs field" style="left:204px;top:1059px">Type of Business</div>
  <div class="abs field" style="left:63px;top:1089px">Website Address</div>
  <div class="abs check"><i></i>Subscribe to newsletter</div>
  <a class="abs btn-signup">SIGNUP</a>

  <h3 class="abs f-title" style="left:376px">At vero eos et accusamus</h3>
  <p class="abs f-text">At vero eos et accusamus et iusto odio dignissimos ducimus qui blanditiis praesentium voluptatum deleniti atque corrupti quos dolores et quas molestias excepturi sint occaecati cupiditate non provident.</p>
  <p class="abs contact-line"><span>Phone :</span> 1300 482 660 &nbsp;<span>Fax :</span> 08 9311 4072</p>
  <div class="abs social">Connect with our social network : <i></i><i></i><i></i></div>

  <h3 class="abs f-title" style="left:649px">Welcome</h3>
  <ul class="abs f-links">
    <li>Home</li><li>About us</li><li>How it works</li><li>Services</li><li>Contact Us</li>
  </ul>
  <p class="abs centered copyright">Copyright © 2016, Brightwell Finance all right reserved.</p>
</div>
</body>
</html>
```